Veterinary Business cards

Redesign Business Card

Information needed on Card:
Hours: Mon-Fri: 4pm -10PM; Sat- Sun- 10 AM- 5PM
Help@tandrelyns.com
www.tandrelyns.com
405-718-2954
4170 SW 38th Ave. okc, ok 73119
*No appointment necessary*

Optional:
Our tag line is "We're here when you need us" - If it fits on the cards.

```html
<!DOCTYPE html>
<html lang="en">
<head>
<meta charset="utf-8">
<title>Tandrelyn Urgent Care – Business Cards</title>
<link href="https://fonts.googleapis.com/css2?family=Montserrat:wght@400;500;700&family=Libre+Baskerville&display=swap" rel="stylesheet">
<style>
  :root {
    --navy: #173a64;
    --orange: #d47a1c;
    --white: #ffffff;
    --ink: #2b2b2b;
    --backdrop: #e9e7e3;
  }
  * { box-sizing: border-box; margin: 0; padding: 0; }
  html, body { width: 1200px; height: 900px; overflow: hidden; }
  body {
    background: var(--backdrop);
    font-family: "Montserrat", Arial, sans-serif;
    position: relative;
  }
  .card {
    position: absolute;
    width: 600px;
    height: 343px;
    box-shadow: 0 10px 28px rgba(0,0,0,0.18);
    overflow: hidden;
  }
  /* Front */
  .card-front {
    left: 70px; top: 70px;
    background: var(--navy);
    color: var(--white);
    display: flex;
    flex-direction: column;
    align-items: center;
    justify-content: center;
  }
  .brand {
    display: flex;
    align-items: center;
    gap: 14px;
  }
  .brand-dot {
    width: 22px; height: 22px;
    border-radius: 50%;
    background: var(--orange);
  }
  .brand-name {
    font-family: "Montserrat", Arial, sans-serif;
    font-weight: 500;
    letter-spacing: 3px;
    text-transform: uppercase;
  }
  .card-front .brand-name { font-size: 30px; color: var(--white); }
  .front-rule {
    width: 360px; height: 1.5px;
    background: var(--white);
    margin: 18px 0 22px;
  }
  .tagline {
    font-family: "Libre Baskerville", Georgia, serif;
    font-size: 19px;
    letter-spacing: 0.5px;
  }
  /* Back */
  .card-back {
    left: 530px; top: 487px;
    background: var(--white);
  }
  .back-brand {
    position: absolute;
    left: 34px; top: 92px;
    width: 250px;
    flex-direction: column;
    align-items: flex-start;
    gap: 10px;
  }
  .card-back .brand-name {
    font-size: 21px;
    color: var(--navy);
    line-height: 1.35;
  }
  .back-rule {
    width: 230px; height: 1.5px;
    background: var(--navy);
  }
  .divider {
    position: absolute;
    left: 300px; top: 40px;
    width: 1px; height: 150px;
    background: linear-gradient(var(--orange), rgba(212,122,28,0.15));
  }
  .contact-list {
    position: absolute;
    left: 320px; top: 44px;
    list-style: none;
    font-size: 14px;
    color: var(--ink);
  }
  .contact-list li {
    display: flex;
    align-items: flex-start;
    gap: 10px;
    margin-bottom: 9px;
    line-height: 1.35;
  }
  .contact-list svg { flex: none; width: 15px; height: 15px; margin-top: 2px; }
  .contact-list .no-icon { padding-left: 25px; }
  .no-appointment {
    position: absolute;
    left: 0; right: 0; top: 226px;
    text-align: center;
    font-weight: 700;
    font-size: 16px;
    color: var(--navy);
  }
  .hours-band {
    position: absolute;
    left: 0; right: 0; bottom: 0;
    height: 52px;
    background: var(--orange);
    border-top: 4px solid var(--navy);
    box-shadow: 0 -4px 0 var(--white);
    color: var(--white);
    font-weight: 700;
    font-size: 17px;
    display: flex;
    align-items: center;
    justify-content: center;
    letter-spacing: 0.3px;
  }
</style>
</head>
<body>

<section class="card card-front">
  <div class="brand">
    <span class="brand-dot"></span>
    <span class="brand-name">Tandrelyn Urgent Care</span>
  </div>
  <div class="front-rule"></div>
  <p class="tagline">We're here when you need us</p>
</section>

<section class="card card-back">
  <div class="brand back-brand">
    <span class="brand-dot"></span>
    <span class="brand-name">Tandrelyn<br>Urgent Care</span>
    <div class="back-rule"></div>
  </div>

  <div class="divider"></div>

  <ul class="contact-list">
    <li>
      <svg viewBox="0 0 24 24" aria-hidden="true"><path fill="#d47a1c" d="M6.6 10.8a15.1 15.1 0 0 0 6.6 6.6l2.2-2.2a1 1 0 0 1 1-.25 11.4 11.4 0 0 0 3.6.57 1 1 0 0 1 1 1V20a1 1 0 0 1-1 1A17 17 0 0 1 3 4a1 1 0 0 1 1-1h3.5a1 1 0 0 1 1 1c0 1.25.2 2.45.57 3.57a1 1 0 0 1-.25 1z"/></svg>
      <span>405-718-2954</span>
    </li>
    <li>
      <svg viewBox="0 0 24 24" aria-hidden="true"><rect x="2" y="5" width="20" height="14" fill="#d47a1c"/><path d="M2 5l10 8 10-8" fill="none" stroke="#fff" stroke-width="1.8"/></svg>
      <span>Help@tandrelyns.com</span>
    </li>
    <li>
      <svg viewBox="0 0 24 24" aria-hidden="true"><circle cx="12" cy="12" r="10" fill="#d47a1c"/><path d="M2 12h20M12 2c3 3 3 17 0 20M12 2c-3 3-3 17 0 20" fill="none" stroke="#fff" stroke-width="1.4"/></svg>
      <span>www.tandrelyns.com</span>
    </li>
    <li class="no-icon">
      <span>4170 SW 38th Ave. okc,<br>ok 73119</span>
    </li>
  </ul>

  <p class="no-appointment">*No appointment necessary*</p>

  <div class="hours-band">Hours: Mon-Fri: 4pm -10PM; Sat- Sun- 10 AM- 5PM</div>
</section>

</body>
</html>
```